Bright Oak Fitness Facility Business Cards

Business Card Design that incorporates the logo and tagline

Target Market(s)

Fitness, People Who Exercise

Contact Information for Business Card

2817 Mossgrove Bend Road
Pinecrest Valley, Oregon 97321
Phone: 541-555-Jump (5867)
www.brightoakfitness.example
info@brightoakfitness.example

Requirements
Must have
• Logo, Address, Website, email and tagline "More Than A Gym". Colors should be red/black/grey/white

```html
<!DOCTYPE html>
<html lang="en">
<head>
<meta charset="utf-8">
<title>Bright Oak Fitness – Business Card</title>
<link rel="stylesheet" href="https://fonts.googleapis.com/css2?family=Exo+2:wght@400;600&family=Dancing+Script:wght@500&display=swap">
<style>
  :root {
    --page-bg: #b3aca3;
    --card-white: #ffffff;
    --brand-red: #ec1c24;
    --brand-black: #0d0d0d;
    --ink: #3a1214;
    --tagline: #ffffff;
  }
  html, body {
    margin: 0;
    padding: 0;
    width: 1200px;
    height: 917px;
    overflow: hidden;
    background: var(--page-bg);
  }
  .business-card {
    position: absolute;
    left: 160px;
    top: 192px;
    width: 880px;
    height: 533px;
    background: var(--card-white);
    overflow: hidden;
    box-shadow: 0 10px 24px rgba(0,0,0,0.25);
  }
  .card-shapes {
    position: absolute;
    inset: 0;
    width: 100%;
    height: 100%;
  }
  .brand-lockup {
    position: absolute;
    left: 36px;
    top: 52px;
    width: 280px;
    text-align: center;
  }
  .brand-mark {
    display: block;
    width: 60px;
    height: 60px;
    margin: 0 auto 22px;
    border-radius: 50%;
    background: var(--brand-red);
  }
  .brand-name {
    font-family: "Exo 2", sans-serif;
    font-weight: 600;
    font-size: 30px;
    line-height: 36px;
    color: var(--brand-red);
    letter-spacing: 0.3px;
    white-space: nowrap;
  }
  .contact-list {
    position: absolute;
    left: 468px;
    top: 148px;
    margin: 0;
    padding: 0;
    list-style: none;
    font-family: "Exo 2", sans-serif;
    font-weight: 400;
    font-size: 25px;
    line-height: 49px;
    color: var(--ink);
    white-space: nowrap;
  }
  .tagline {
    position: absolute;
    left: 414px;
    top: 482px;
    font-family: "Dancing Script", cursive;
    font-weight: 500;
    font-size: 31px;
    line-height: 40px;
    color: var(--tagline);
    white-space: nowrap;
  }
</style>
</head>
<body>
  <div class="business-card">
    <svg class="card-shapes" viewBox="0 0 429 260" preserveAspectRatio="none" aria-hidden="true">
      <polygon class="red-field" fill="var(--brand-red)" points="263,0 429,0 429,260 243,260 258,233 106,233"/>
      <polygon class="black-stroke" fill="var(--brand-black)" points="228,0 263,0 106,233 258,233 243,260 53,260"/>
    </svg>

    <div class="brand-lockup">
      <span class="brand-mark"></span>
      <div class="brand-name">Bright Oak Fitness</div>
    </div>

    <ul class="contact-list">
      <li>2817 Mossgrove Bend Road</li>
      <li>Pinecrest Valley, Oregon 97321</li>
      <li>Phone: 541-555-Jump (5867)</li>
      <li>www.brightoakfitness.example</li>
      <li>info@brightoakfitness.example</li>
    </ul>

    <div class="tagline">More Than A Gym</div>
  </div>
</body>
</html>
```